Quillory Nest Business Card

I need a business card design. We are a collaborate online training company. Our colors are gray and green. Our website is QuilloryNest.com

I would like an area for a profile picture within the card

```html
<!DOCTYPE html>
<html lang="en">
<head>
<meta charset="utf-8">
<title>Quillory Nest Business Card</title>
<link rel="stylesheet" href="https://fonts.googleapis.com/css2?family=Open+Sans:wght@400;600;700&display=swap">
<style>
  :root {
    --backdrop: #e7e5e1;
    --card: #313131;
    --green: #8cc63f;
    --white: #ffffff;
    --text: #eeeeee;
    --rule: #555555;
  }
  * { margin: 0; padding: 0; box-sizing: border-box; }
  html, body {
    width: 1200px; height: 1000px; overflow: hidden;
    background: var(--backdrop);
    font-family: "Open Sans", Arial, sans-serif;
  }
  .canvas { position: relative; width: 1200px; height: 1000px; }
  .card {
    position: absolute; left: 243px; width: 708px; height: 404px;
    background: var(--card);
    box-shadow: 0 6px 18px rgba(0,0,0,0.25);
  }
  .card--front { top: 84px; }
  .card--back { top: 526px; }

  .wordmark {
    position: absolute; display: flex; align-items: center;
    color: var(--white); font-weight: 700; letter-spacing: -0.5px; white-space: nowrap;
  }
  .wordmark__dot { border-radius: 50%; background: var(--green); flex: none; }
  .card--front .wordmark { left: 140px; top: 140px; font-size: 50px; gap: 20px; }
  .card--front .wordmark__dot { width: 64px; height: 64px; }
  .card--back .wordmark { left: 56px; top: 168px; font-size: 30px; gap: 12px; }
  .card--back .wordmark__dot { width: 38px; height: 38px; }

  .divider {
    position: absolute; left: 353px; top: 120px; width: 1px; height: 170px;
    background: linear-gradient(to bottom, transparent, var(--rule) 20%, var(--rule) 80%, transparent);
  }
  .contact { position: absolute; left: 380px; top: 110px; color: var(--text); font-size: 16px; line-height: 20px; }
  .contact__name { color: var(--green); font-weight: 700; font-size: 17px; letter-spacing: 1px; }
  .contact__role { margin-bottom: 14px; }
  .contact__address { margin-bottom: 14px; }
  .contact__line { display: flex; align-items: center; gap: 7px; height: 25px; }
  .contact__line svg { width: 12px; height: 12px; flex: none; }
</style>
</head>
<body>
<main class="canvas">
  <section class="card card--front">
    <div class="wordmark"><span class="wordmark__dot"></span>QuilloryNest</div>
  </section>

  <section class="card card--back">
    <div class="wordmark"><span class="wordmark__dot"></span>QuilloryNest</div>
    <div class="divider"></div>
    <div class="contact">
      <p class="contact__name">MARLA PENWICK</p>
      <p class="contact__role">Founder</p>
      <p class="contact__address">482 W Harlow Ave. Suite 7<br>Brindle, Arizona 85390</p>
      <p class="contact__line">
        <svg viewBox="0 0 12 12"><path fill="#8cc63f" d="M2.5 1l2 2.2-1 1.3c.6 1.3 1.7 2.4 3 3l1.3-1 2.2 2-1.2 1.5C5 9.8 2.2 7 1 3.2z"/></svg>
        (555) 284-3916
      </p>
      <p class="contact__line">
        <svg viewBox="0 0 12 12"><rect x="1" y="2.5" width="10" height="7" fill="#8cc63f"/><path d="M1 2.5l5 4 5-4" fill="none" stroke="#313131" stroke-width="1"/></svg>
        info@quillorynest.com
      </p>
      <p class="contact__line">
        <svg viewBox="0 0 12 12" fill="none" stroke="#8cc63f" stroke-width="1"><circle cx="6" cy="6" r="4.8"/><ellipse cx="6" cy="6" rx="2" ry="4.8"/><path d="M1.2 6h9.6"/></svg>
        www.quillorynest.com
      </p>
    </div>
  </section>
</main>
</body>
</html>
```